Corvint Property Management Vendor Recruiting Email

We need a digital flyer to email and post on Social media to attract new vendors to our website to apply to complete maintenance work on our clients homes. I have one flyer we had produced recently that we are un-happy with. It is attached.

The example given is what we do not want!! We do not want any of the pictures used from the existing one

Target Market(s)

Construction companies and handyman

Industry/Entity Type

Residential maintenance and repairs

Requirements
Must have
• Join our team as the header not become a vendor

```html
<!DOCTYPE html>
<html lang="en">
<head>
<meta charset="UTF-8">
<title>Corvint Property Management – Join Our Team</title>
<link href="https://fonts.googleapis.com/css2?family=Fredoka:wght@700&family=Mulish:wght@600;700&family=Oswald:wght@600&family=Roboto+Condensed:wght@700&family=Fira+Sans+Condensed:ital,wght@1,600&display=swap" rel="stylesheet">
<style>
  :root {
    --page: #ffffff;
    --flyer: #674f7f;
    --frame: #ffffff;
    --accent: #d4e02b;
    --text: #ffffff;
    --phone-blue: #1e76bb;
    --tag-purple: #5b2a8c;
    --bar: #000000;
    --brand-box: #0e0c1a;
    --band: #8a87c4;
  }
  * { margin: 0; padding: 0; box-sizing: border-box; }
  html, body { width: 1200px; height: 1200px; overflow: hidden; background: var(--page); }
  .flyer {
    position: absolute; left: 40px; top: 98px; width: 1120px; height: 1004px;
    background: var(--flyer); color: var(--text); overflow: hidden;
  }
  .frame {
    position: absolute; left: 31px; top: 18px; width: 1059px; height: 966px;
    border: 2px solid var(--frame); border-radius: 24px; overflow: hidden;
  }
  .headline {
    position: absolute; left: 0; right: 0; top: 82px; text-align: center;
    font-family: "Fredoka", sans-serif; font-weight: 700; font-size: 86px;
    letter-spacing: 1px; line-height: 1; white-space: nowrap;
  }
  .divider {
    position: absolute; left: 511px; top: 225px; width: 2px; height: 426px; background: var(--frame);
  }
  .benefits, .requirements { position: absolute; list-style: none; font-family: "Mulish", sans-serif; font-weight: 600; }
  .benefits { left: 35px; top: 240px; width: 445px; font-size: 25px; line-height: 32px; }
  .benefits li { position: relative; padding-left: 26px; margin-bottom: 32px; }
  .requirements { left: 543px; top: 326px; width: 510px; font-size: 23.5px; line-height: 28px; }
  .requirements li { position: relative; padding-left: 26px; margin-bottom: 23px; }
  .benefits li::before, .requirements li::before {
    content: ""; position: absolute; left: 0; top: 10px; width: 11px; height: 11px;
    border-radius: 50%; background: var(--accent);
  }
  .req-title {
    position: absolute; left: 543px; top: 222px; width: 500px;
    font-family: "Oswald", sans-serif; font-weight: 600; font-size: 36px; line-height: 48px;
    color: var(--accent); text-transform: uppercase;
  }
  .contact { position: absolute; left: 93px; top: 680px; transform: rotate(-3deg); transform-origin: left bottom; }
  .contact-tag {
    display: inline-block; margin-left: 80px; background: #fff; color: var(--tag-purple);
    font-family: "Oswald", sans-serif; font-weight: 600; font-size: 26px; padding: 2px 22px 6px;
    border-radius: 4px 4px 0 0;
  }
  .contact-phone {
    display: block; width: 528px; height: 124px; background: var(--phone-blue);
    border: 3px solid #fff; border-radius: 6px; box-shadow: 2px 3px 4px rgba(0,0,0,.35);
    font-family: "Roboto Condensed", sans-serif; font-weight: 700; font-size: 86px;
    line-height: 118px; text-align: center; color: #fff; white-space: nowrap; overflow: hidden;
  }
  .footer-bar {
    position: absolute; left: 0; right: 0; top: 886px; height: 56px; background: var(--bar);
  }
  .footer-band { position: absolute; left: 0; right: 0; top: 942px; bottom: 0; background: var(--band); }
  .website {
    position: absolute; left: 122px; top: 898px; display: flex; align-items: center; gap: 10px;
    font-family: "Fira Sans Condensed", sans-serif; font-style: italic; font-weight: 600; font-size: 26px;
    white-space: nowrap;
  }
  .brand-box {
    position: absolute; left: 704px; top: 798px; width: 257px; height: 146px; background: var(--brand-box);
    display: flex; align-items: center; justify-content: center; text-align: center;
    font-family: "Mulish", sans-serif; font-weight: 700; font-size: 20px; line-height: 26px;
    letter-spacing: 1px; text-transform: uppercase; color: #fff;
  }
</style>
</head>
<body>
  <main class="flyer">
    <div class="frame">
      <h1 class="headline">JOIN OUR TEAM TODAY!</h1>

      <ul class="benefits">
        <li>95% approval rating on all submitted estimates.</li>
        <li>Guaranteed work volume.</li>
        <li>Material purchasing program to help vendors with low capital or no or bad credit.</li>
        <li>Weekly secure direct deposit with net 30 payment terms.</li>
      </ul>

      <div class="divider"></div>

      <h2 class="req-title">Requirements to become a<br>vendor</h2>
      <ul class="requirements">
        <li>Auto insurance</li>
        <li>Certificate of general liability insurance</li>
        <li>Workman’s Compensation or state issued exemption letter</li>
        <li>Drive License or state issued ID card</li>
        <li>Coverage area</li>
        <li>Any speciality Licenses</li>
      </ul>

      <div class="contact">
        <span class="contact-tag">CONTACT</span>
        <span class="contact-phone">555-214-0382</span>
      </div>

      <div class="footer-bar"></div>
      <div class="footer-band"></div>
      <div class="website">
        <svg width="30" height="30" viewBox="0 0 30 30" fill="none" stroke="#fff" stroke-width="2">
          <circle cx="15" cy="15" r="13"/>
          <ellipse cx="15" cy="15" rx="6" ry="13"/>
          <line x1="2" y1="15" x2="28" y2="15"/>
        </svg>
        <span>www.corvintpropertymanagement.com</span>
      </div>
      <div class="brand-box">Corvint<br>Property<br>Management</div>
    </div>
  </main>
</body>
</html>
```